Design 3 banner stands for trade show graphics

31'W x 81'H - design should be clean and pop. We work with higher ed and k12 (high school) industry so our audience is students, administrators, and such. One of the attached graphics has the concept of our 3 banner stands. 1 - KelvaroWorks 2 - Graphic (what we like - multiracial, neatly dressed, differ. ages, world behind, swoosh at the bottom which mimics our look on flyers - see attachment). what we don't like - green color which doesn't go w/ our look, words on the image. Our 2 products are used to help schools proctor exams and measure student learner readiness. I'd like to see 2 variations. One colorful with red and purple popping somehow coordinating with our literature w/o being matchy matchy and the other option a bit more muted or subdued in color. We want to look professional and not like a preschool using bright colors but visually appealing nonetheless.

Target Market(s)

Educators, faculty, administrators, college students, all 50 states

Industry/Entity Type

Preschool

Font styles to use
Serif
Sans Serif

Colors
6b449b
ec2027

Requirements
Must have
• 3 individual banner stands 2 with logos and info and the other one with image
image should be multiracial
Nice to have
• some kind of world/globe image with the ticks marks around our "S" in our logos kind of like ovals exemplifying smarter or better
Should not have
• No outdated clothing on people; no curly cutesy fonts,

```html
<!DOCTYPE html>
<html lang="en">
<head>
<meta charset="utf-8">
<title>Trade Show Banner Stands – Distance Learning</title>
<link rel="stylesheet" href="https://fonts.googleapis.com/css2?family=Open+Sans:wght@400;600;700&display=swap">
<style>
  :root {
    --brand-red: #ec2027;
    --brand-purple: #6b449b;
    --ink: #1f1f1f;
    --ink-soft: #2e2e2e;
    --band-grey: #cfcfcf;
    --panel-grey: #c9c9c9;
    --paper: #ffffff;
    --backdrop: #e9e9e9;
    --map-tone: #d9d9d9;
  }
  * { box-sizing: border-box; margin: 0; padding: 0; }
  html, body {
    width: 1200px; height: 1000px; overflow: hidden;
    background: var(--backdrop);
    font-family: "Open Sans", Arial, sans-serif;
    color: var(--ink);
  }
  .banner-set {
    position: absolute; left: 198px; top: 88px;
    display: flex; gap: 5px;
  }
  .stand {
    width: 266px; height: 712px; background: var(--paper);
    position: relative; overflow: hidden;
    box-shadow: 0 2px 6px rgba(0,0,0,0.12);
  }

  /* product stands */
  .brand-head { height: 117px; padding: 52px 0 0 40px; }
  .brand-name { font-size: 22px; font-weight: 600; line-height: 1; letter-spacing: -0.3px; }
  .brand-name--red { color: var(--brand-red); }
  .brand-name--purple { color: var(--brand-purple); font-size: 19px; }
  .brand-tagline { font-size: 9px; color: #555; margin: 4px 0 0 80px; }
  .pitch {
    height: 200px; color: #fff; font-size: 15.5px; line-height: 27px;
    padding: 42px 20px 0 34px;
  }
  .pitch--red { background: var(--brand-red); }
  .pitch--purple { background: var(--brand-purple); padding: 34px 22px 0 28px; font-size: 15px; }
  .benefits-bar {
    height: 48px; background: var(--band-grey);
    display: flex; align-items: center; padding-left: 24px;
    font-size: 19px; font-weight: 600; margin-top: 5px;
  }
  .benefits-bar .dot {
    width: 20px; height: 20px; border-radius: 50%; background: #fff;
    margin-right: 34px;
  }
  .benefit-list { list-style: none; padding: 32px 10px 0 25px; }
  .benefit-list li {
    position: relative; padding-left: 30px; font-size: 13.5px;
    line-height: 1.25; margin-bottom: 15px; color: var(--ink-soft);
  }
  .benefit-list li::before {
    content: ""; position: absolute; left: 0; top: 3px;
    width: 11px; height: 11px; background: var(--ink);
  }

  /* centre stand */
  .stand--feature { background: var(--panel-grey); }
  .feature-head { height: 140px; text-align: center; padding-top: 62px; }
  .parent-name { font-size: 16px; font-weight: 700; color: var(--ink); letter-spacing: 1px; line-height: 1; }
  .feature-title { font-size: 19px; font-weight: 700; margin-top: 22px; line-height: 1; }
  .feature-photo {
    height: 302px;
    background: linear-gradient(180deg, #f4f4f4 0%, var(--map-tone) 45%, #8a6d5c 75%, #3f4a6a 100%);
  }
  .feature-gap { height: 22px; }
  .feature-copy {
    background: var(--paper); height: 98px; text-align: center;
    font-size: 15.5px; font-weight: 600; line-height: 26px; padding-top: 12px;
  }
  .feature-wave {
    height: 150px;
    background: linear-gradient(180deg, var(--paper) 0%, #e2e2e2 30%, var(--panel-grey) 65%);
  }
</style>
</head>
<body>
  <main class="banner-set">

    <section class="stand stand--measure">
      <header class="brand-head">
        <div class="brand-name brand-name--red">KelvaroWorks</div>
        <div class="brand-tagline">Learning readiness indicator</div>
      </header>
      <p class="pitch pitch--red">Increase retention by identifying at-risk students based on non-congitive indicators of learner success</p>
      <h2 class="benefits-bar"><span class="dot"></span>Benefits</h2>
      <ul class="benefit-list">
        <li>Custom User interface</li>
        <li>Used by 500+ schools</li>
        <li>Taken by 2.5+ million students</li>
        <li>Used for student services, orientation, or advising</li>
      </ul>
    </section>

    <section class="stand stand--feature">
      <header class="feature-head">
        <div class="parent-name">Norvale</div>
        <h1 class="feature-title">Distance Learning</h1>
      </header>
      <div class="feature-photo" role="img" aria-label="World map above a diverse group of neatly dressed students, one holding a tablet"></div>
      <div class="feature-gap"></div>
      <div class="feature-copy">
        Distance Learning<br>and online degrees<br>from the comfort of your home
      </div>
      <div class="feature-wave" role="img" aria-label="Soft grey swoosh across the foot of the banner"></div>
    </section>

    <section class="stand stand--proctor">
      <header class="brand-head">
        <div class="brand-name brand-name--purple">TestHarbor</div>
        <div class="brand-tagline">Testing Management System</div>
      </header>
      <p class="pitch pitch--purple">Organize the workflow for all types of proctoring including on-campus testing centers, virtual proctoring, and/or human proctoring.</p>
      <h2 class="benefits-bar"><span class="dot"></span>Benefits</h2>
      <ul class="benefit-list">
        <li>Integrated into your LMS</li>
        <li>Dashboard of all proctoring activity</li>
        <li>FREE to schools to use</li>
        <li>Improve the use of other proctoring technologies</li>
      </ul>
    </section>

  </main>
</body>
</html>
```